Corvex

Electronic Repairs for OEM's Industrial electronic repairs, consumer audio visual, Projectors

Target Market(s)

manufacturer of electronics (OEM), business, Government, then Consumer

Industry/Entity Type

Electronic Repair

Contact Information for Business Card

Board Repair, Projectors

Font styles to use
Serif

Colors
0054AA
0677BA
7BADD7
CADEEF
E8F1F8

Requirements
Must have
• projector, led wall image
Nice to have
• professional looking business card.
Should not have
• unsure

```html
<!DOCTYPE html>
<html lang="en">
<head>
<meta charset="utf-8">
<title>Corvex Electronic Repairs – Business Card</title>
<link rel="stylesheet" href="https://fonts.googleapis.com/css2?family=Montserrat:wght@400;700;800&family=Poppins:wght@400&family=Roboto+Condensed:wght@400;700&display=swap">
<style>
  :root {
    --brand-blue: #0054AA;
    --accent-blue: #0677BA;
    --soft-blue: #7BADD7;
    --pale-blue: #CADEEF;
    --mist: #E8F1F8;
    --ink: #111111;
    --card: #ffffff;
    --page: #e6e9ee;
  }
  * { margin: 0; padding: 0; box-sizing: border-box; }
  html, body { width: 1200px; height: 840px; overflow: hidden; }
  body { background: var(--page); position: relative; font-family: "Montserrat", sans-serif; }

  .business-card {
    position: absolute; left: 100px; top: 135px;
    width: 1000px; height: 570px;
    background: var(--card);
    border-radius: 40px;
    overflow: hidden;
    box-shadow: 0 12px 30px rgba(0,0,0,.18);
  }
  .side-band { position: absolute; inset: 0; width: 100%; height: 100%; }

  .photo-circle {
    position: absolute; border-radius: 50%;
    border: 6px solid #fff;
    box-shadow: 0 4px 12px rgba(0,0,0,.25);
  }
  .photo-projector { left: 590px; top: 60px; width: 220px; height: 220px; z-index: 2;
    background: radial-gradient(circle at 40% 55%, #d9d2ff 0, #4a7fa6 14%, #1c5c80 45%, #0b2c44 100%); }
  .photo-ledwall { left: 740px; top: 165px; width: 220px; height: 220px;
    background: radial-gradient(circle at 70% 20%, #e0296f 0, #8c1d52 35%, #2a1830 70%, #111 100%); }
  .photo-board { left: 640px; top: 290px; width: 220px; height: 220px;
    background: radial-gradient(circle at 45% 40%, #cfe3f5 0, #4b86c4 35%, #174f8e 75%, #0c2f5a 100%); }

  .brand { position: absolute; left: 75px; top: 45px; }
  .brand-name {
    font-weight: 800; font-size: 96px; line-height: 1;
    color: var(--brand-blue);
  }
  .brand-sub {
    font-weight: 400; font-size: 32px; line-height: 1;
    color: var(--accent-blue); margin-top: 4px; letter-spacing: .5px;
  }

  .tagline {
    position: absolute; left: 80px; top: 200px;
    font-weight: 700; font-size: 22px; line-height: 1.22;
    color: var(--brand-blue);
  }

  .services { position: absolute; left: 85px; top: 300px; list-style: none; }
  .services li {
    font-family: "Poppins", sans-serif; font-size: 25px; line-height: 36px;
    color: var(--ink); display: flex; align-items: center; gap: 14px;
  }
  .services svg { width: 24px; height: 24px; flex: none; }

  .contact { position: absolute; left: 80px; top: 424px; }
  .contact-phone {
    font-weight: 800; font-size: 38px; line-height: 1.1;
    color: var(--brand-blue);
  }
  .contact-email {
    font-family: "Roboto Condensed", sans-serif; font-weight: 700;
    font-size: 34px; line-height: 1.15; color: var(--ink);
  }
  .contact-address {
    font-family: "Roboto Condensed", sans-serif; font-weight: 400;
    font-size: 25px; line-height: 1.25; color: var(--ink);
  }
</style>
</head>
<body>
  <div class="business-card">
    <svg class="side-band" viewBox="0 0 1000 570" aria-hidden="true">
      <path d="M640 0 C 760 60, 700 330, 860 570 L1000 570 L1000 0 Z" fill="var(--brand-blue)"/>
      <path d="M640 0 C 690 20, 712 60, 718 110" fill="none" stroke="var(--accent-blue)" stroke-width="10"/>
    </svg>

    <div class="photo-circle photo-projector" role="img" aria-label="Photo of a ceiling-mounted projector with its lens lit"></div>
    <div class="photo-circle photo-ledwall" role="img" aria-label="Close-up photo of a curved magenta LED wall panel"></div>
    <div class="photo-circle photo-board" role="img" aria-label="Close-up photo of a blue electronic circuit board"></div>

    <div class="brand">
      <div class="brand-name">CORVEX</div>
      <div class="brand-sub">ELECTRONIC REPAIRS</div>
    </div>

    <p class="tagline">Electronic Repairs for OEM's<br>Industrial electronic repairs,<br>consumer audio visual, Projectors</p>

    <ul class="services">
      <li><svg viewBox="0 0 24 24"><circle cx="12" cy="12" r="12" fill="var(--brand-blue)"/><path d="M6.5 12.5l3.5 3.5 7.5-8" fill="none" stroke="#fff" stroke-width="3" stroke-linecap="round" stroke-linejoin="round"/></svg>Projector</li>
      <li><svg viewBox="0 0 24 24"><circle cx="12" cy="12" r="12" fill="var(--brand-blue)"/><path d="M6.5 12.5l3.5 3.5 7.5-8" fill="none" stroke="#fff" stroke-width="3" stroke-linecap="round" stroke-linejoin="round"/></svg>Led wall image</li>
      <li><svg viewBox="0 0 24 24"><circle cx="12" cy="12" r="12" fill="var(--brand-blue)"/><path d="M6.5 12.5l3.5 3.5 7.5-8" fill="none" stroke="#fff" stroke-width="3" stroke-linecap="round" stroke-linejoin="round"/></svg>Board Repair</li>
    </ul>

    <div class="contact">
      <div class="contact-phone">CALL US 555-210 4830</div>
      <div class="contact-email">info@corvexelectronicrepairs.com</div>
      <div class="contact-address">4219 Willow Bend Road, Juneau, Alaska 99801</div>
    </div>
  </div>
</body>
</html>
```